Kestrel Wiring - Electrician company flyers for new clients

I want a flyer that will be dropped into mailboxes and will hopefully stand out more that the ones i have tried to mock up. I have attached my latest design to give you an idea but it is rather boring.

The aim is obviously to entice new customers into calling me for any electrical work, mainly domestic but i also do commercial work.
I will also upload a photo of my business card so that it can be used as a reference and my website is www.kestrelwiring.co.nz for any extra information.

Ideally the flyer will be DL size
measurements from printmorrow is that's any help
Document Trim Size
99 x 210 mm
1169 x 2480 pixels
Full Bleed Size
102 x 213 mm
1205 x 2516 pixels

Target Market(s)

Domestic electrical works

Industry/Entity Type

Electrician

Requirements
Must have
• all of my contact details -
• Dean Forsyth
• Dean@kestrelwiring.co.nz
• 027 3815 942
• www.kestrelwiring.co.nz
• A little write up similar to the one written on my draft but there's probably alot of room for improvement as my writing skills are lacking.
Nice to have
• clear and concise writing so that people wont throw it away before reading

```html
<!DOCTYPE html>
<html lang="en">
<head>
<meta charset="utf-8">
<title>Kestrel Wiring – DL Flyer</title>
<link href="https://fonts.googleapis.com/css2?family=Montserrat:wght@600;700&family=Mulish:ital,wght@0,400;0,600;0,700;1,400&display=swap" rel="stylesheet">
<style>
  :root {
    --backdrop: #959394;
    --paper: #ffffff;
    --brand-blue: #20a0dc;
    --brand-grey: #7b7b7d;
    --ink-dark: rgba(40, 40, 42, 0.72);
    --ink-blue: rgba(32, 160, 220, 0.85);
    --outline: #8a8a8c;
  }
  * { margin: 0; padding: 0; box-sizing: border-box; }
  html, body { width: 1200px; height: 1000px; overflow: hidden; }
  body { background: var(--backdrop); position: relative; font-family: "Mulish", sans-serif; }

  .flyer {
    position: absolute; top: 39px; width: 435px; height: 922px;
    background: var(--paper); overflow: hidden;
  }
  .flyer--front { left: 138px; }
  .flyer--back { left: 628px; }

  .brand {
    position: absolute; top: 0; left: 0; width: 100%; height: 156px;
    display: flex; align-items: center; justify-content: center;
  }
  .brand__name {
    font-family: "Montserrat", sans-serif; font-weight: 700; font-size: 38px;
    color: var(--brand-blue); letter-spacing: 0.5px;
  }

  .hero-photo {
    position: absolute; top: 156px; left: 0; width: 100%; height: 450px;
    background: linear-gradient(135deg, #c9cccd 0%, #8f9a9c 35%, #4c5a63 65%, #2f3a44 100%);
  }

  .shapes { position: absolute; top: 0; left: 0; }

  .headline { position: absolute; left: 29px; top: 197px; }
  .headline__bar {
    display: block; background: var(--ink-dark); color: #fff;
    font-family: "Montserrat", sans-serif; font-weight: 700;
    padding: 0 18px; margin-bottom: 7px; white-space: nowrap;
  }
  .headline__bar--a { font-size: 27px; line-height: 41px; width: 172px; }
  .headline__bar--b { font-size: 27px; line-height: 45px; width: 346px; }
  .headline__bar--c { font-size: 37px; line-height: 47px; width: 378px; }
  .headline__tag {
    display: block; background: var(--ink-blue); color: #fff;
    font-weight: 600; font-size: 16.5px; line-height: 41px;
    padding: 0 18px; width: 320px; white-space: nowrap;
  }

  .contact { position: absolute; left: 29px; top: 604px; color: #fff; }
  .contact__lead { font-family: "Montserrat", sans-serif; font-weight: 600; font-size: 17px; }
  .contact__phone { font-family: "Montserrat", sans-serif; font-weight: 700; font-size: 35px; line-height: 44px; letter-spacing: 1px; }
  .contact__email { font-weight: 600; font-size: 16.5px; margin-top: 8px; }
  .contact__note { font-style: italic; font-size: 11px; margin-top: 2px; }

  .web-pill {
    position: absolute; left: 88px; top: 836px; width: 259px; height: 46px;
    border: 2px solid var(--outline); border-radius: 23px;
    display: flex; align-items: center; justify-content: center;
    color: var(--brand-blue); font-weight: 700; font-size: 16.5px;
  }

  .about { position: absolute; left: 66px; top: 210px; width: 305px; color: #fff; }
  .about__intro { font-size: 17px; line-height: 22.5px; }
  .about__intro strong { font-weight: 700; }
  .about__rule { border: 0; border-top: 1px solid rgba(255,255,255,0.8); width: 277px; margin: 26px 0 22px; }
  .about__list { list-style: none; }
  .about__item { display: flex; gap: 14px; margin-bottom: 20px; }
  .about__item svg { flex: none; margin-top: 1px; }
  .about__item p { font-weight: 600; font-size: 14.5px; line-height: 18.6px; }
  .about__closing { font-style: italic; font-size: 17px; margin-top: 6px; }
</style>
</head>
<body>

<section class="flyer flyer--front">
  <header class="brand"><span class="brand__name">Kestrel Wiring</span></header>

  <div class="hero-photo" role="img" aria-label="Photo of an electrician in a hi-vis vest sorting coloured wires at a wall box"></div>

  <svg class="shapes" width="435" height="922" viewBox="0 0 435 922" aria-hidden="true">
    <path d="M0 500 Q180 582 435 590" fill="none" stroke="#8c8c8e" stroke-width="6"/>
    <path d="M0 507 Q180 588 435 595 L435 790 L0 790 Z" fill="#20a0dc"/>
    <path d="M0 765 C170 745 330 720 435 697 L435 712 C330 745 150 790 0 812 Z" fill="#7b7b7d"/>
    <path d="M0 812 C150 790 330 745 435 712 L435 922 L0 922 Z" fill="#ffffff"/>
    <path d="M255 762 L435 703 L435 716 Z" fill="#ffffff"/>
  </svg>

  <div class="headline">
    <span class="headline__bar headline__bar--a">RELIABLE</span>
    <span class="headline__bar headline__bar--b">AND PROFESSIONAL</span>
    <span class="headline__bar headline__bar--c">ELECTRICIANS</span>
    <span class="headline__tag">Customer Satisfaction Guaranteed</span>
  </div>

  <div class="contact">
    <p class="contact__lead">CONTACT US TODAY!</p>
    <p class="contact__phone">027 3815 942</p>
    <p class="contact__email">Dean@kestrelwiring.co.nz</p>
    <p class="contact__note">We look forward to serving you!</p>
  </div>

  <div class="web-pill">www.kestrelwiring.co.nz</div>
</section>

<section class="flyer flyer--back">
  <header class="brand"><span class="brand__name">Kestrel Wiring</span></header>

  <svg class="shapes" width="435" height="922" viewBox="0 0 435 922" aria-hidden="true">
    <rect x="0" y="156" width="435" height="634" fill="#20a0dc"/>
    <path d="M0 765 C170 745 330 720 435 697 L435 712 C330 745 150 790 0 812 Z" fill="#7b7b7d"/>
    <path d="M0 812 C150 790 330 745 435 712 L435 922 L0 922 Z" fill="#ffffff"/>
    <path d="M255 762 L435 703 L435 716 Z" fill="#ffffff"/>
  </svg>

  <div class="about">
    <p class="about__intro"><strong>Specializing in residential and commercial electrical services, we are dedicated to providing customer service that is second to none.</strong> Whether you need a small wiring fix or the full installation , we can get the job done right.</p>
    <hr class="about__rule">
    <ul class="about__list">
      <li class="about__item">
        <svg width="23" height="23" viewBox="0 0 23 23" aria-hidden="true"><path d="M19 10.5 A8.5 8.5 0 1 1 14.5 3.6" fill="none" stroke="#fff" stroke-width="2"/><path d="M6.5 11 L10.5 15 L21 4" fill="none" stroke="#fff" stroke-width="2.4" stroke-linecap="round" stroke-linejoin="round"/></svg>
        <p>We provide you with a full consultation to explain your available options so that you can choose the scope of work that’s right for your home or business - and your budget.</p>
      </li>
      <li class="about__item">
        <svg width="23" height="23" viewBox="0 0 23 23" aria-hidden="true"><path d="M19 10.5 A8.5 8.5 0 1 1 14.5 3.6" fill="none" stroke="#fff" stroke-width="2"/><path d="M6.5 11 L10.5 15 L21 4" fill="none" stroke="#fff" stroke-width="2.4" stroke-linecap="round" stroke-linejoin="round"/></svg>
        <p>Based in Harlow Bay, We are local Electricians with our main aim to keep our work and communication to a very high standard.</p>
      </li>
    </ul>
    <p class="about__closing">We look forward to serving you!</p>
  </div>

  <div class="web-pill">www.kestrelwiring.co.nz</div>
</section>

</body>
</html>
```